design a construction company business card

Design business card around our logo. Card must have all the typical info: name, title, address, phone, email, business name, etc. Somewhere on the card I would like to see our motto "Built on integrity... Inspired by commitment." Consider adding a splash of bright orange to the card to complement the blues and silvers/grays in the logo. We are open to metallic inks, textures, etc. We would like to see options on both light and dark backgrounds. The font in the logo is Euro Technic Extended Regular.

```html
<!DOCTYPE html>
<html lang="en">
<head>
<meta charset="utf-8">
<title>Halvern Builders – Business Card</title>
<link href="https://fonts.googleapis.com/css2?family=Open+Sans:wght@400;600;700&display=swap" rel="stylesheet">
<style>
  :root {
    --backdrop: #2b2c2e;
    --blue-deep: #2b3f9e;
    --blue-mid: #2a5cb8;
    --blue-bright: #1a7bc6;
    --ink-blue: #2346a8;
    --ink-gray: #6b6e73;
    --rule-gray: #c9cbce;
    --paper: #ffffff;
  }
  * { margin: 0; padding: 0; box-sizing: border-box; }
  html, body {
    width: 1200px; height: 892px; overflow: hidden;
    background: var(--backdrop);
    font-family: "Open Sans", Arial, sans-serif;
  }
  .canvas { position: relative; width: 1200px; height: 892px; }

  .card {
    position: absolute; width: 525px; height: 300px;
    box-shadow: 0 14px 30px rgba(0,0,0,0.45);
    overflow: hidden;
  }

  /* Front */
  .card-front {
    left: 70px; top: 90px;
    background: radial-gradient(ellipse 70% 80% at 62% 38%, var(--blue-bright) 0%, var(--blue-mid) 45%, var(--blue-deep) 100%);
  }
  .card-front .brand-name {
    position: absolute; right: 40px; bottom: 56px;
    color: var(--paper); font-weight: 700; font-size: 26px;
    letter-spacing: 1px; text-align: right; line-height: 1.15;
  }

  /* Back */
  .card-back { left: 610px; top: 500px; background: var(--paper); }
  .card-back .band { position: absolute; left: 0; top: 0; width: 525px; height: 300px; }
  .card-back .brand-name {
    position: absolute; left: 34px; top: 128px;
    color: var(--ink-blue); font-weight: 700; font-size: 25px;
    letter-spacing: 1px; line-height: 1.15;
    display: flex; align-items: center; gap: 10px;
  }
  .brand-square { width: 14px; height: 14px; background: var(--ink-blue); flex: none; }
  .divider {
    position: absolute; left: 268px; top: 62px; width: 1px; height: 130px;
    background: var(--rule-gray);
  }
  .contact {
    position: absolute; left: 290px; top: 54px;
    color: var(--ink-gray); font-size: 12.5px; line-height: 1.45;
  }
  .contact .person-name { color: var(--ink-blue); font-weight: 700; font-size: 17px; line-height: 1.1; }
  .contact .person-title { font-size: 12px; letter-spacing: 0.5px; margin-bottom: 8px; }
  .contact .line { display: flex; align-items: center; gap: 8px; }
  .contact svg { width: 12px; height: 12px; fill: var(--ink-blue); flex: none; }
  .website {
    position: absolute; right: 40px; bottom: 13px;
    color: var(--paper); font-size: 12px; letter-spacing: 5px;
  }
</style>
</head>
<body>
<div class="canvas">

  <section class="card card-front">
    <div class="brand-name">HALVERN<br>BUILDERS, INC.</div>
  </section>

  <section class="card card-back">
    <svg class="band" viewBox="0 0 525 300" aria-hidden="true">
      <defs>
        <linearGradient id="bandFill" x1="0" y1="0" x2="1" y2="0">
          <stop offset="0" stop-color="#2b3f9e"/>
          <stop offset="1" stop-color="#2a5cb8"/>
        </linearGradient>
      </defs>
      <polygon points="0,274 525,250 525,300 0,300" fill="url(#bandFill)"/>
    </svg>

    <div class="brand-name"><span class="brand-square"></span>HALVERN<br>BUILDERS, INC.</div>

    <div class="divider"></div>

    <div class="contact">
      <div class="person-name">MARCUS ELLERY</div>
      <div class="person-title">PRESIDENT</div>
      <div>2217 Ashford Lane</div>
      <div>Lindale, NY 11040</div>
      <div class="line">
        <svg viewBox="0 0 24 24"><path d="M6.6 10.8a15 15 0 0 0 6.6 6.6l2.2-2.2a1 1 0 0 1 1-.25 11.4 11.4 0 0 0 3.6.57 1 1 0 0 1 1 1V20a1 1 0 0 1-1 1A17 17 0 0 1 3 4a1 1 0 0 1 1-1h3.5a1 1 0 0 1 1 1c0 1.250.2 2.45.57 3.6a1 1 0 0 1-.25 1z"/></svg>
        555 0142 7789
      </div>
      <div class="line">
        <svg viewBox="0 0 24 24"><path d="M2 5h20v14H2z M2 5l10 8 10-8" fill="none" stroke="#2346a8" stroke-width="2.4"/></svg>
        marcus@halvern.com
      </div>
    </div>

    <div class="website">www.halvern.com</div>
  </section>

</div>
</body>
</html>
```